Venture firm needs flyer to attract Sales Professionals as Advisors

Creation of either a pdf Flyer or Brochure.
The target audience are senior sales professionals of the Information Technology industry. The flyer needs to come across highly professional, business oriented, positive. Text for the brochure is attached. The colors/graphics should align with Tormid Ventures corporate appearance: www.tormid-example.ventures

Target Market(s)

Sales Professionals in the Information Technology Industry

Industry/Entity Type

Information Technology

Font styles to use
Other font styles liked:
• Raleway

Requirements
Must have
• fitting the corporate look and feel: www.tormid-example.ventures

```html
<!DOCTYPE html>
<html lang="en">
<head>
<meta charset="utf-8">
<title>Tormid Ventures – Achieving Growth</title>
<link href="https://fonts.googleapis.com/css2?family=Questrial&display=swap" rel="stylesheet">
<style>
  :root {
    --navy-deep: #132c40;
    --navy: #0f3a5e;
    --blue-brand: #3a7bb0;
    --blue-mid: #3572a0;
    --blue-light: #3c89bd;
    --blue-slate: #3a6782;
    --ink: #1b2a3a;
    --paper: #ffffff;
    --snow-bright: #fbfbfd;
    --snow-light: #e9ecf1;
    --snow-shade: #a9b1bf;
    --snow-deep: #7f899a;
  }
  html, body {
    margin: 0;
    padding: 0;
    overflow: hidden;
    background: var(--paper);
  }
  .flyer {
    position: relative;
    width: 849px;
    height: 1200px;
    overflow: hidden;
    background: var(--paper);
    font-family: "Questrial", "Raleway", sans-serif;
  }
  .flyer-art {
    position: absolute;
    inset: 0;
    width: 849px;
    height: 1200px;
  }
  .masthead {
    position: absolute;
    left: 60px;
    top: 52px;
    z-index: 2;
  }
  .brand-name {
    margin: 0;
    font-weight: 400;
    font-size: 62px;
    line-height: 1;
    letter-spacing: 1.5px;
    color: var(--navy-deep);
    white-space: nowrap;
  }
  .brand-name .brand-first {
    color: var(--blue-brand);
  }
  .tagline {
    margin: 12px 0 0 8px;
    font-size: 22.5px;
    letter-spacing: 0.8px;
    color: var(--ink);
    white-space: nowrap;
  }
  .headline {
    margin: 6px 0 0 7px;
    font-weight: 400;
    font-size: 52px;
    line-height: 1;
    letter-spacing: 0.6px;
    color: var(--ink);
    white-space: nowrap;
  }
</style>
</head>
<body>
<main class="flyer">
  <svg class="flyer-art" viewBox="0 0 849 1200" xmlns="http://www.w3.org/2000/svg">
    <defs>
      <linearGradient id="snow-tone" x1="0.2" y1="0" x2="0.75" y2="1">
        <stop offset="0" stop-color="var(--snow-light)"/>
        <stop offset="0.25" stop-color="var(--snow-shade)"/>
        <stop offset="0.5" stop-color="var(--snow-deep)"/>
        <stop offset="0.68" stop-color="var(--snow-light)"/>
        <stop offset="1" stop-color="var(--snow-bright)"/>
      </linearGradient>
    </defs>

    <polygon class="corner-rule" points="836,0 849,0 849,2 434,446 428,446" fill="var(--navy-deep)"/>
    <polygon class="corner-block" points="849,9 849,446 440,446" fill="var(--navy-deep)"/>

    <g role="img" aria-label="Photo of a mountaineer in a yellow and green jacket holding an ice axe, standing on a snowy ridge above a frozen lake, seen from behind">
      <polygon points="430,446 849,446 849,1200 528,1200 212,852 140,768" fill="url(#snow-tone)"/>
    </g>

    <polygon class="band-navy" points="232,446 430,446 140,768 40,660" fill="var(--navy)"/>
    <polygon class="band-blue" points="0,700 40,660 140,768 212,852 528,1200 0,1200" fill="var(--blue-mid)"/>
    <polygon class="facet-light" points="0,700 40,660 212,852 130,940 26,840 0,870" fill="var(--blue-light)"/>
    <polygon class="facet-slate" points="26,840 130,745 130,940" fill="var(--blue-slate)"/>
    <polygon class="facet-slate" points="0,870 26,840 26,1066 0,1095" fill="var(--blue-slate)"/>
    <polygon class="facet-light" points="0,1095 26,1066 26,1200 0,1200" fill="var(--blue-light)" opacity="0.6"/>
  </svg>

  <header class="masthead">
    <h1 class="brand-name"><span class="brand-first">TORMID</span> VENTURES</h1>
    <p class="tagline">INVESTING IN GLOBAL GO-TO-MARKET STRATEGIES</p>
    <h2 class="headline">ACHIEVING GROWTH</h2>
  </header>
</main>
</body>
</html>
```